Redesign responsive website and logo for webshop platform

Redesign our applications old website with a new clean, crisp modern looking style that is responsive.

Our application is a cloud based, free ecommerce platform that lets users set up their own webshops within minutes. (Similar to Bramvik https://bramvik.example/l/sell)

Our old website: http://sv.kelporia.example/

I need redesigned HTML + CSS for the following three pages:
* Landing Page:
(Old page: http://sv.kelporia.example/)
I have attached a mockup of a proposed layout/structure for the landing page.
- Pricing comparision/features page
(Old page http://sv.kelporia.example/t/funktioner)
- Generic "article" page:
(Old page http://sv.kelporia.example/d/redigerasida)

The pages must responsive using HTML 5/CSS 3 (I prefer Bootstrap 3 if possible).

I also need a redesign of the logotype.

If you have any questions don't hesitate to ask and we will provide whatever is needed to you.

Logo Text

Kelporia

Coding

Coded - Design and coding required

Number of Pages Required

3 page

Font styles to use
Serif
Sans Serif

```html
<!DOCTYPE html>
<html lang="sv">
<head>
<meta charset="utf-8">
<title>Kelporia – Start a free webshop</title>
<link href="https://fonts.googleapis.com/css2?family=Roboto:wght@300;400&display=swap" rel="stylesheet">
<style>
:root{
  --navy:#0c2033;
  --ink:#1b2a3a;
  --muted:#8a8f96;
  --white:#ffffff;
  --paper:#f6f6f6;
  --amber:#fbbc2c;
  --ring:#e3e3e3;
}
*{box-sizing:border-box;margin:0;padding:0}
html,body{width:823px;height:1200px;overflow:hidden}
body{position:relative;font-family:"Roboto",Arial,sans-serif;color:var(--ink);background:var(--white)}
.abs{position:absolute}

/* hero */
.hero{left:0;top:0;width:823px;height:355px;background:var(--navy);color:var(--white)}
.brand{font-size:19px;font-weight:400;letter-spacing:.5px;color:var(--white)}
.hero .brand{left:40px;top:22px}
.login{right:40px;top:28px;font-size:9.5px;color:var(--white);text-decoration:none}
.hero-title{left:0;width:823px;top:132px;text-align:center;font-size:37px;font-weight:400;letter-spacing:.3px}
.divider{left:330px;top:184px}
.lead{left:0;width:823px;top:216px;text-align:center;font-size:11px;line-height:16px}
.cta{left:338px;top:264px;width:148px;height:35px;border-radius:18px;background:var(--amber);color:var(--white);font-size:11.5px;font-weight:300;text-align:center;line-height:35px;text-decoration:none}

/* features */
.features{left:0;top:355px;width:823px;height:497px;background:var(--paper)}
.card{width:235px;height:201px;background:var(--white);text-align:center}
.card .badge{position:absolute;left:96px;top:33px;width:42px;height:42px;border-radius:50%;border:1px solid var(--ring);display:flex;align-items:center;justify-content:center}
.card h3{position:absolute;left:0;width:235px;top:94px;font-size:11.8px;font-weight:400;letter-spacing:.2px}
.card p{position:absolute;left:20px;width:195px;top:120px;font-size:9.8px;line-height:14px}

/* small features */
.mini{width:220px}
.mini svg{position:absolute;left:0;top:0}
.mini h4{position:absolute;top:0;font-size:11.6px;font-weight:400;white-space:nowrap}
.mini p{position:absolute;top:20px;width:200px;font-size:9.6px;line-height:14px;color:var(--muted)}

/* footer */
.footer{left:0;top:1095px;width:823px;height:105px;background:var(--navy);color:var(--white)}
.footer .brand{left:114px;top:15px}
.contact{display:flex;align-items:center;gap:7px;font-size:12px;color:var(--white)}
.contact .ring{width:32px;height:32px;border-radius:50%;border:2px solid var(--white);display:flex;align-items:center;justify-content:center}
.copy{left:0;width:823px;top:84px;text-align:center;font-size:9px}
</style>
</head>
<body>

<header class="abs hero">
  <div class="abs brand">KELPORIA</div>
  <a class="abs login" href="#">Have an account? Log in</a>
  <h1 class="abs hero-title">Start a free webshop</h1>
  <svg class="abs divider" width="164" height="20" viewBox="0 0 164 20">
    <line x1="0" y1="11" x2="68" y2="11" stroke="#fff" stroke-width="1"/>
    <line x1="94" y1="11" x2="164" y2="11" stroke="#fff" stroke-width="1"/>
    <polygon points="82,2 84.6,8 91,8.4 86,12.6 87.6,19 82,15.5 76.4,19 78,12.6 73,8.4 79.4,8" fill="#fff"/>
  </svg>
  <p class="abs lead">Kelporia is a service that allows you to launch a complete online store.<br>The service is free and has everything needed to get you started with your business and sell products online.</p>
  <a class="abs cta" href="#">Create an account</a>
</header>

<section class="abs features">
  <article class="abs card" style="left:40px;top:36px">
    <div class="badge"><svg width="14" height="14" viewBox="0 0 14 14"><circle cx="7" cy="7" r="5.5" fill="none" stroke="#0c2033" stroke-width="2"/><path d="M7 4v3h2.5" fill="none" stroke="#0c2033" stroke-width="1.5"/></svg></div>
    <h3>GET STARTED IN 5 MINUTES</h3>
    <p>Lorem ipsum dolor sit amet, consectetur adipiscing elit, sed do eiusmod tempor incididunt ut labore.</p>
  </article>
  <article class="abs card" style="left:294px;top:36px">
    <div class="badge"><svg width="14" height="14" viewBox="0 0 14 14"><circle cx="7" cy="7" r="6" fill="#0c2033"/><path d="M4 4c2 0 2 2 3 3s-1 3 0 4M9 2.5c0 2 2 2 3 2.5" fill="none" stroke="#fff" stroke-width="1"/></svg></div>
    <h3>CREATE A FREE ONLINE STORE</h3>
    <p>Lorem ipsum dolor sit amet, consectetur adipiscing elit, sed do eiusmod tempor incididunt ut labore.</p>
  </article>
  <article class="abs card" style="left:549px;top:36px">
    <div class="badge"><svg width="15" height="14" viewBox="0 0 15 14"><rect x="1" y="1" width="13" height="12" fill="none" stroke="#0c2033" stroke-width="1.6"/><line x1="1" y1="4" x2="14" y2="4" stroke="#0c2033" stroke-width="1.6"/><line x1="7.5" y1="4" x2="7.5" y2="13" stroke="#0c2033" stroke-width="1.6"/></svg></div>
    <h3>INTUITIVE USER INTERFACE</h3>
    <p>Lorem ipsum dolor sit amet, consectetur adipiscing elit, sed do eiusmod tempor incididunt ut labore.</p>
  </article>
  <article class="abs card" style="left:40px;top:257px">
    <div class="badge"><svg width="14" height="14" viewBox="0 0 14 14"><circle cx="6" cy="6" r="4.2" fill="none" stroke="#0c2033" stroke-width="2"/><line x1="9" y1="9" x2="13" y2="13" stroke="#0c2033" stroke-width="2.4"/></svg></div>
    <h3>SEARCH ENGINE OPTIMIZED</h3>
    <p>Lorem ipsum dolor sit amet, consectetur adipiscing elit, sed do eiusmod tempor incididunt ut labore.</p>
  </article>
  <article class="abs card" style="left:294px;top:257px">
    <div class="badge"><svg width="14" height="14" viewBox="0 0 14 14"><path d="M2 12l1-3.5 7-7 2.5 2.5-7 7z" fill="#0c2033"/></svg></div>
    <h3>DESIGNA YOUR SHOP</h3>
    <p>Lorem ipsum dolor sit amet, consectetur adipiscing elit, sed do eiusmod tempor incididunt ut labore.</p>
  </article>
  <article class="abs card" style="left:549px;top:257px">
    <div class="badge"><svg width="16" height="14" viewBox="0 0 16 14"><path d="M1 1v12h14" fill="none" stroke="#0c2033" stroke-width="1.4"/><rect x="4" y="7" width="2" height="5" fill="#0c2033"/><rect x="7" y="4" width="2" height="8" fill="#0c2033"/><rect x="10" y="6" width="2" height="6" fill="#0c2033"/><rect x="13" y="3" width="1.5" height="9" fill="#0c2033"/></svg></div>
    <h3>SMART DASHBOARD</h3>
    <p>Lorem ipsum dolor sit amet, consectetur adipiscing elit, sed do eiusmod tempor incididunt ut labore.</p>
  </article>
</section>

<section>
  <div class="abs mini" style="left:40px;top:893px">
    <svg width="21" height="16" viewBox="0 0 21 16"><path d="M5 15a4 4 0 0 1-.5-8A5.5 5.5 0 0 1 15 5a4.5 4.5 0 0 1 1 10z" fill="#0c2033"/></svg>
    <h4 style="left:30px">SMALL FEATURE 1</h4>
    <p style="left:30px">Lorem ipsum dolor sit amet, consectetur adipiscing elit. Nullam id ipsum varius, tincidunt odio nec, placerat enim.</p>
  </div>
  <div class="abs mini" style="left:294px;top:893px">
    <svg width="21" height="16" viewBox="0 0 21 16"><rect x="3" y="2" width="15" height="10" fill="none" stroke="#0c2033" stroke-width="1.5"/><line x1="0" y1="14" x2="21" y2="14" stroke="#0c2033" stroke-width="2"/></svg>
    <h4 style="left:30px">SMALL FEATURE 2</h4>
    <p style="left:30px">Lorem ipsum dolor sit amet, consectetur adipiscing elit. Nullam id ipsum varius, tincidunt odio nec, placerat enim.</p>
  </div>
  <div class="abs mini" style="left:549px;top:893px">
    <svg width="17" height="17" viewBox="0 0 17 17"><line x1="4" y1="8.5" x2="13" y2="3.5" stroke="#0c2033" stroke-width="1.8"/><line x1="4" y1="8.5" x2="13" y2="13.5" stroke="#0c2033" stroke-width="1.8"/><circle cx="4" cy="8.5" r="3.2" fill="#0c2033"/><circle cx="13" cy="3.5" r="3" fill="#0c2033"/><circle cx="13" cy="13.5" r="3" fill="#0c2033"/></svg>
    <h4 style="left:25px">SMALL FEATURE 3</h4>
    <p style="left:25px">Lorem ipsum dolor sit amet, consectetur adipiscing elit. Nullam id ipsum varius, tincidunt odio nec, placerat enim.</p>
  </div>
  <div class="abs mini" style="left:40px;top:987px">
    <svg width="20" height="17" viewBox="0 0 20 17"><rect x="1" y="3.5" width="18" height="13" rx="1.5" fill="#0c2033"/><rect x="6.5" y="1" width="7" height="3" fill="none" stroke="#0c2033" stroke-width="1.5"/><line x1="5" y1="4" x2="5" y2="16" stroke="#fff" stroke-width="1"/><line x1="15" y1="4" x2="15" y2="16" stroke="#fff" stroke-width="1"/></svg>
    <h4 style="left:29px">SMALL FEATURE 4</h4>
    <p style="left:29px">Lorem ipsum dolor sit amet, consectetur adipiscing elit. Nullam id ipsum varius, tincidunt odio nec, placerat enim.</p>
  </div>
  <div class="abs mini" style="left:294px;top:987px">
    <svg width="21" height="16" viewBox="0 0 21 16"><path d="M1 14V2h6l2 2h7v3M1 14l3.5-7H20l-3.5 7z" fill="none" stroke="#0c2033" stroke-width="1.4" stroke-linejoin="round"/></svg>
    <h4 style="left:30px">SMALL FEATURE 5</h4>
    <p style="left:30px">Lorem ipsum dolor sit amet, consectetur adipiscing elit. Nullam id ipsum varius, tincidunt odio nec, placerat enim.</p>
  </div>
  <div class="abs mini" style="left:549px;top:987px">
    <h4 style="left:28px">SMALL FEATURE 6</h4>
    <p style="left:28px">Lorem ipsum dolor sit amet, consectetur adipiscing elit. Nullam id ipsum varius, tincidunt odio nec, placerat enim.</p>
  </div>
</section>

<footer class="abs footer">
  <div class="abs brand">KELPORIA</div>
  <a class="abs contact" href="#" style="left:342px;top:20px"><span class="ring"></span>Kelporia på Chirpline</a>
  <a class="abs contact" href="#" style="left:596px;top:20px"><span class="ring"><svg width="14" height="10" viewBox="0 0 14 10"><rect x="0" y="0" width="14" height="10" rx="1" fill="#fff"/><path d="M0.5 0.8L7 6l6.5-5.2" fill="none" stroke="#0c2033" stroke-width="1.3"/></svg></span>info@kelporia.example</a>
  <p class="abs copy">© 2016 Vantrel | Support | Documentation</p>
</footer>

</body>
</html>
```